Pebble Lane real estate investment company needs a poster design

We would like a poster design size 18 x 24.
Poster wording -
I WANT TO BUY YOUR ( finish with logo) logo uploaded
website- www.pebblelane-homes.example
phone # 555-217-8843 ( color red for the phone number)
we would like to see the poster on 2 different backgrounds
Yellow background
White background
horizontal

```html
<!DOCTYPE html>
<html lang="en">
<head>
<meta charset="utf-8">
<title>Pebble Lane – I Want To Buy Your House</title>
<link href="https://fonts.googleapis.com/css2?family=Poppins:wght@700;800;900&display=swap" rel="stylesheet">
<style>
  :root {
    --sky: #8fb0d6;
    --wood-red: #8a2a22;
    --ground: #b8ab96;
    --yellow: #ffdd00;
    --red: #e8202a;
    --ink: #111111;
    --slate: #4a4a4a;
  }
  html, body {
    margin: 0;
    padding: 0;
    overflow: hidden;
    background: #ffffff;
  }
  .poster {
    position: relative;
    width: 1200px;
    height: 900px;
    overflow: hidden;
    font-family: "Poppins", sans-serif;
  }
  .hero-photo {
    position: absolute;
    inset: 0;
    background: linear-gradient(180deg, var(--sky) 0%, #a9c2de 12%, var(--wood-red) 22%, #6e2a24 45%, #7b6f62 60%, var(--ground) 85%, #a99c86 100%);
  }
  .yellow-wedge {
    position: absolute;
    inset: 0;
    width: 1200px;
    height: 900px;
  }
  .headline-panel {
    position: absolute;
    left: 492px;
    top: 314px;
    width: 708px;
    height: 438px;
    box-sizing: border-box;
    background: var(--yellow);
    border-top: 7px solid var(--red);
    border-left: 7px solid var(--red);
    text-align: center;
  }
  .headline-lead {
    position: absolute;
    left: 0;
    width: 624px;
    top: 28px;
    margin: 0;
    font-size: 136px;
    font-weight: 900;
    line-height: 1;
    color: var(--slate);
    letter-spacing: 2px;
  }
  .headline-sub {
    position: absolute;
    left: 0;
    width: 624px;
    top: 178px;
    margin: 0;
    font-size: 70px;
    font-weight: 900;
    line-height: 1;
    color: var(--slate);
    letter-spacing: -1px;
  }
  .brand-name {
    position: absolute;
    left: 0;
    width: 624px;
    top: 268px;
    margin: 0;
    font-size: 76px;
    font-weight: 900;
    line-height: 1;
    color: var(--ink);
  }
  .contact {
    position: absolute;
    left: 470px;
    width: 700px;
    top: 766px;
    text-align: center;
  }
  .contact-phone {
    margin: 0;
    font-size: 52px;
    font-weight: 800;
    color: var(--red);
    line-height: 1.1;
    letter-spacing: 1px;
  }
  .contact-web {
    margin: 2px 0 0;
    font-size: 28px;
    font-weight: 700;
    color: var(--ink);
    line-height: 1.2;
  }
  .pointer {
    position: absolute;
    top: 790px;
  }
  .pointer-left { left: 486px; }
  .pointer-right { left: 1036px; }
</style>
</head>
<body>
<main class="poster">
  <div class="hero-photo" role="img" aria-label="Photo of a weathered red wooden abandoned house with a collapsed porch in a dry field under a blue sky"></div>

  <svg class="yellow-wedge" viewBox="0 0 1200 900" aria-hidden="true">
    <polygon points="1200,8 1200,900 320,900" fill="var(--yellow)"/>
  </svg>

  <section class="headline-panel">
    <h1 class="headline-lead">I WANT</h1>
    <p class="headline-sub">TO BUY YOUR</p>
    <p class="brand-name">Pebble Lane</p>
  </section>

  <svg class="pointer pointer-left" width="112" height="26" viewBox="0 0 112 26" aria-hidden="true">
    <line x1="4" y1="13" x2="104" y2="13" stroke="var(--red)" stroke-width="4" stroke-linecap="round"/>
    <polyline points="88,3 106,13 88,23" fill="none" stroke="var(--red)" stroke-width="4" stroke-linejoin="round" stroke-linecap="round"/>
  </svg>
  <svg class="pointer pointer-right" width="112" height="26" viewBox="0 0 112 26" aria-hidden="true">
    <line x1="8" y1="13" x2="108" y2="13" stroke="var(--red)" stroke-width="4" stroke-linecap="round"/>
    <polyline points="24,3 6,13 24,23" fill="none" stroke="var(--red)" stroke-width="4" stroke-linejoin="round" stroke-linecap="round"/>
  </svg>

  <div class="contact">
    <p class="contact-phone">555-217-8843</p>
    <p class="contact-web">www.pebblelane-homes.example</p>
  </div>
</main>
</body>
</html>
```